Marlow Bridge needs a brochure review

We are a company operating in more than 10 countries that, since 1972, has the ambitious and innovative objective to stimulate foreign language learning by discovering different countries and cultures, through training courses tailored to individual needs
We need a layout review of our brochure in order to make the content clearer, immediate and appealing and, at the same time, make the layout more modern and young.
The pages we need are: the cover and pages 3, 5, 7, 20, 21, 22, 23, 34, 36, 37. You will find our actual brochure pdf as attachment

Target Market(s)

Students and families, business

Industry/Entity Type

It Company

Requirements
Must have
• The same written information as the actual one.
• Blue and green colours.
• The cover must be simple, elegant and clean but new and effective. In addition to the cover the pages you should review are number :2, 3, 4, 5, 6, 7. Feel free to use new background, images and new layout for the text.

```html
<!DOCTYPE html>
<html lang="it">
<head>
<meta charset="utf-8">
<title>Marlow Bridge – Promozioni</title>
<link rel="stylesheet" href="https://fonts.googleapis.com/css2?family=Roboto:wght@400;500;700;900&family=Roboto+Condensed:wght@300;400&display=swap">
<style>
  :root{
    --red:#f25c5a;
    --orange:#f89c21;
    --blue:#0089bf;
    --green:#00a651;
    --panel:#f2f2f2;
    --ink:#333333;
    --white:#ffffff;
    --bar-dark:#363636;
    --bar-grey:#9b9b9b;
  }
  *{box-sizing:border-box;margin:0;padding:0}
  html,body{width:944px;height:1200px;overflow:hidden;background:var(--white)}
  .page{position:relative;width:944px;height:1200px;font-family:"Roboto",Arial,sans-serif;color:var(--ink)}

  .offer{position:absolute;width:297px;background:var(--panel);border-bottom:9px solid var(--accent)}
  .offer--early-plus{left:128px;top:105px;height:444px;--accent:var(--red)}
  .offer--early{left:523px;top:105px;height:444px;--accent:var(--orange)}
  .offer--safe{left:128px;top:574px;height:444px;--accent:var(--blue)}
  .offer--campus{left:521px;top:574px;height:444px;--accent:var(--green)}

  .offer__head{position:relative;height:119px;background:var(--accent)}
  .offer__title{position:absolute;left:75px;top:26px}
  .offer__tier{display:block;font-size:14px;font-weight:500;color:var(--white);letter-spacing:.2px}
  .offer__brand{display:block;font-size:20px;font-weight:400;color:var(--ink);margin-top:2px;white-space:nowrap}
  .offer__square{position:absolute;left:232px;top:18px;width:26px;height:26px;background:var(--white)}

  .badge{position:absolute;left:88px;top:79px;width:118px;height:118px;border-radius:50%;background:var(--white);text-align:center;padding-top:20px}
  .badge__label{font-size:12px;font-weight:700;color:#222}
  .badge__amount{font-size:21px;font-weight:900;color:var(--accent);margin-top:2px;letter-spacing:.3px}
  .badge__date{font-size:8.5px;font-weight:700;color:#222;line-height:11px;margin-top:2px}
  .badge__deposit{font-size:7.5px;font-weight:700;color:var(--accent);margin-top:2px}

  .offer__text{position:absolute;left:14px;right:14px;top:206px;font-family:"Roboto Condensed",Arial,sans-serif;font-weight:300;font-size:13.3px;line-height:18.4px;color:#333;text-align:justify;hyphens:auto}

  .promo-bar__shadow{position:absolute;left:51px;top:1104px;width:867px;height:42px;background:var(--bar-grey)}
  .promo-bar{position:absolute;left:38px;top:1112px;width:867px;height:42px;background:var(--bar-dark)}
  .promo-bar__text{position:absolute;left:39px;top:14px;font-family:"Roboto Condensed",Arial,sans-serif;font-size:11.5px;color:var(--white)}
  .folio{position:absolute;left:765px;top:1179px;font-family:"Roboto Condensed",Arial,sans-serif;font-size:10.5px;color:#222}
  .folio b{font-weight:700}
</style>
</head>
<body>
<main class="page">

  <section class="offer offer--early-plus">
    <header class="offer__head">
      <div class="offer__title"><span class="offer__tier">Super Early</span><span class="offer__brand">Marlow Bridge</span></div>
      <span class="offer__square" aria-hidden="true"></span>
      <div class="badge">
        <div class="badge__label">SCONTO</div>
        <div class="badge__amount">€ 500</div>
        <div class="badge__date">Per iscrizioni ento<br>il 20 dicembre 2016</div>
        <div class="badge__deposit">acconto €299</div>
      </div>
    </header>
    <p class="offer__text">Prenotando la tua vacanza studio entro questa data, ti garantirai uno sconto di €130 per le destinazioni Europee, o €80 per le destinazioni USA. In regalo per te anche la garanzia Cambio Idea: fino al 28/02/2017 potrai annullare per qualsiasi motivo, senza nessuna penale. Avrai inoltre l’offerta SafeTrip, del valore di €270, in omaggio (scopri tutti i vantaggi della garanzia a pagina 9). Se hai scelto una destinazione Campus, in regalo per te il programma Campus Move &amp; Play (del valore di €50 a settimana).</p>
  </section>

  <section class="offer offer--early">
    <header class="offer__head">
      <div class="offer__title"><span class="offer__tier">Early</span><span class="offer__brand">Marlow Bridge</span></div>
      <span class="offer__square" aria-hidden="true"></span>
      <div class="badge">
        <div class="badge__label">SCONTO</div>
        <div class="badge__amount">€ 470</div>
        <div class="badge__date">Per iscrizioni ento<br>il 26 gennaio 2017</div>
        <div class="badge__deposit">acconto €299</div>
      </div>
    </header>
    <p class="offer__text">Prenotando la tua vacanza studio entro questa data, avrai uno sconto di €100 per le destinazioni Europee e di €50 per le destinazioni USA. Avrai inoltre l’offerta SafeTrip, del valore di €270, in omaggio (scopri tutti i vantaggi della garanzia a pagina 9). Se hai scelto una destinazione Campus, in regalo per te il programma Campus Move &amp; Play (del valore di €50 a settimana).</p>
  </section>

  <section class="offer offer--safe">
    <header class="offer__head">
      <div class="offer__title"><span class="offer__tier">SafeTrip</span><span class="offer__brand">Marlow Bridge</span></div>
      <span class="offer__square" aria-hidden="true"></span>
      <div class="badge">
        <div class="badge__label">SCONTO</div>
        <div class="badge__amount">€ 370</div>
        <div class="badge__date">Per iscrizioni ento<br>il 28 febbraio 2017</div>
      </div>
    </header>
    <p class="offer__text">Prenotando la tua vacanza studio entro questa data otterrai gratuitamente la speciale garanzia SafeTrip, del valore di €100 per ogni settimana di soggiorno. La garanzia ti permette di annullare la vacanza studio fino a 15 giorni prima della partenza, ti protegge contro le oscillazioni dei cambi valutari e ti permette di estendere gratuitamente la polizza USA (del valore di €70). Scopri tutti i vantaggi della garanzia Safe Trip a pagina 9. Se hai scelto una destinazione Campus, in regalo per te il programma Campus Move &amp; Play (del valore di €50 a settimana).</p>
  </section>

  <section class="offer offer--campus">
    <header class="offer__head">
      <div class="offer__title"><span class="offer__tier">Campus</span><span class="offer__brand">Marlow Bridge</span></div>
      <span class="offer__square" aria-hidden="true"></span>
      <div class="badge">
        <div class="badge__label">SCONTO</div>
        <div class="badge__amount">€ 100</div>
        <div class="badge__date">Per iscrizioni ento<br>il 10 marzo 2017</div>
      </div>
    </header>
    <p class="offer__text">Prenotando la tua vacanza studio entro questa data, avrai uno sconto di €100 per le destinazioni Europee e di €50 per le destinazioni USA. Avrai inoltre l’offerta SafeTrip, del valore di €270, in omaggio (scopri tutti i vantaggi della garanzia a pagina 9). Se hai scelto una destinazione Campus, in regalo per te il programma Campus Move &amp; Play (del valore di €50 a settimana).</p>
  </section>

  <div class="promo-bar__shadow" aria-hidden="true"></div>
  <div class="promo-bar"><span class="promo-bar__text">Come fare a usufruire delle promozioni? Vedi a pag. 94</span></div>
  <div class="folio">Marlow Bridge Estate 2017 - <b>7</b></div>

</main>
</body>
</html>
```